I need a book cover design for a 6 x 9 85 page book called "Lanterns Along the Harbor Road" It is subtitled "Quiet Lessons from an Orchard Keeper and Her Curious Village Neighbors"
On the front cover I'd like a picture of a mountain with fire and lightening, With the title and the subtitle. By Dale Purvin near the bottom of the page.
On the back cover I'd like and image of two stone tablets The one of the left should be title "Fiscal Responsibility" and it should have the first five commandments. The one of the right should be titled "Loving-Kindness" and it should have the other five commandments. The commandments are in the attached file, and should be kept in the order I have them.

```html
<!DOCTYPE html>
<html lang="en">
<head>
<meta charset="utf-8">
<title>Lanterns Along the Harbor Road — Cover Spread</title>
<link rel="stylesheet" href="https://fonts.googleapis.com/css2?family=Oswald:wght@400;500&display=swap">
<style>
  :root {
    --back-top: #e98468;
    --back-mid: #a83a63;
    --back-low: #4a1a34;
    --back-base: #1f0d16;
    --sky-top: #b3497c;
    --sky-mid: #8c3460;
    --sky-glow: rgba(245, 200, 215, 0.55);
    --ember: rgba(235, 60, 50, 0.55);
    --slope-top: #7a2e34;
    --slope-mid: #4c2020;
    --slope-base: #1c0d0b;
    --spine-top: #c25a7e;
    --spine-base: #2a1116;
    --tablet-light: rgba(170, 80, 110, 0.78);
    --tablet-dark: rgba(40, 14, 26, 0.85);
    --ink-light: #fbeef0;
    --ink-tablet: #f6e2e6;
    --ink-outline: #3a1320;
  }
  * { margin: 0; padding: 0; box-sizing: border-box; }
  html, body { width: 1200px; height: 850px; overflow: hidden; background: #1a0b12; }
  .spread {
    position: relative;
    width: 1200px;
    height: 850px;
    font-family: "Oswald", "Arial Narrow", sans-serif;
    text-transform: uppercase;
    overflow: hidden;
  }

  /* Back cover */
  .back-cover {
    position: absolute; left: 0; top: 0; width: 576px; height: 850px;
    background: linear-gradient(180deg, var(--back-top) 0%, var(--back-mid) 38%, var(--back-low) 72%, var(--back-base) 100%);
  }
  .tablet {
    position: absolute;
    background: linear-gradient(180deg, var(--tablet-light) 0%, rgba(110, 40, 70, 0.8) 55%, var(--tablet-dark) 100%);
  }
  .tablet--left { left: 14px; top: 128px; width: 282px; height: 560px; border-radius: 48% 48% 10px 10px / 14% 14% 10px 10px; }
  .tablet--right { left: 291px; top: 206px; width: 272px; height: 505px; border-radius: 48% 48% 10px 10px / 14% 14% 10px 10px; }

  .tablet-text {
    position: absolute; top: 0; height: 850px;
    color: var(--ink-tablet);
    font-size: 17px; font-weight: 500; letter-spacing: 0.06em;
    list-style: none; text-align: center;
    text-shadow: 0 1px 2px rgba(40, 10, 20, 0.6);
  }
  .tablet-text--left { left: 20px; width: 272px; }
  .tablet-text--right { left: 292px; width: 272px; }
  .tablet-text li { position: absolute; left: 0; width: 100%; line-height: 22px; white-space: nowrap; }

  /* Spine */
  .spine {
    position: absolute; left: 576px; top: 0; width: 45px; height: 850px;
    background: linear-gradient(180deg, var(--spine-top) 0%, #7c2c48 45%, var(--spine-base) 100%);
    display: flex; justify-content: center; align-items: flex-start;
  }
  .spine-text {
    writing-mode: vertical-rl;
    margin-top: 24px;
    font-size: 33px; font-weight: 500; letter-spacing: 0.05em;
    color: var(--ink-light);
    -webkit-text-stroke: 1px var(--ink-outline);
    white-space: nowrap;
    line-height: 45px;
  }
  .spine-author { margin-top: 30px; }

  /* Front cover */
  .front-cover {
    position: absolute; left: 621px; top: 0; width: 579px; height: 850px;
  }
  .front-scene {
    position: absolute; inset: 0;
    background:
      radial-gradient(ellipse 34% 34% at 80% 28%, var(--sky-glow), transparent 72%),
      radial-gradient(ellipse 20% 14% at 16% 31%, var(--ember), transparent 75%),
      linear-gradient(180deg,
        var(--sky-top) 0%,
        var(--sky-mid) 28%,
        #a0485e 40%,
        var(--slope-top) 47%,
        var(--slope-mid) 62%,
        #33170f 80%,
        var(--slope-base) 100%);
  }
  .front-title {
    position: absolute; left: 0; top: 32px; width: 100%;
    text-align: center; color: var(--ink-light); font-weight: 500;
    -webkit-text-stroke: 1px var(--ink-outline);
    line-height: 1.2;
  }
  .front-title__line { display: block; }
  .front-title__line--first { font-size: 60px; letter-spacing: 0.05em; }
  .front-title__line--second { font-size: 64px; letter-spacing: 0.05em; }

  .front-subtitle {
    position: absolute; left: 0; top: 388px; width: 100%;
    text-align: center; color: var(--ink-light);
    font-size: 32px; font-weight: 500; letter-spacing: 0.05em;
    -webkit-text-stroke: 0.6px var(--ink-outline);
  }
  .front-subtitle__line { display: block; line-height: 46px; }
  .front-subtitle__line--last { margin-top: 52px; }
  .front-author {
    position: absolute; left: 0; top: 722px; width: 100%;
    text-align: center; color: var(--ink-light);
    font-size: 62px; font-weight: 500; letter-spacing: 0.05em;
    -webkit-text-stroke: 1px var(--ink-outline);
  }
</style>
</head>
<body>
<div class="spread">

  <section class="back-cover" role="img" aria-label="Stormy sunset sky with lightning over a dark plain and two standing stone tablets">
    <div class="tablet tablet--left" role="img" aria-label="Left stone tablet"></div>
    <div class="tablet tablet--right" role="img" aria-label="Right stone tablet"></div>

    <ul class="tablet-text tablet-text--left">
      <li style="top:188px">Fiscal Responsibility</li>
      <li style="top:232px">The First Commandment</li>
      <li style="top:276px">Tax Financial Settlements,</li>
      <li style="top:302px">&nbsp;&nbsp;Not Income</li>
      <li style="top:337px">The Second Commandment</li>
      <li style="top:364px">Balance the Budget</li>
      <li style="top:428px">The Third Commandment</li>
      <li style="top:458px">Payoff the Debt</li>
      <li style="top:504px">The Fourth Commandment</li>
      <li style="top:540px">Implement Banking 2.0</li>
      <li style="top:602px">The Fifth Commandment</li>
      <li style="top:643px">Charge No Interest</li>
    </ul>

    <ul class="tablet-text tablet-text--right">
      <li style="top:249px">Loving-Kindness</li>
      <li style="top:286px">The Sixth Commandment</li>
      <li style="top:313px">Provide for the Poor</li>
      <li style="top:362px">The Seventh Commandment</li>
      <li style="top:400px">Provide Free Healthcare</li>
      <li style="top:452px">The Eighth Commandment</li>
      <li style="top:481px">Provide Free Higher</li>
      <li style="top:527px">The Ninth Commandment</li>
      <li style="top:564px">Provide a National Income</li>
      <li style="top:630px">The Tenth Commandment</li>
      <li style="top:663px">Invest in Other Nations</li>
    </ul>
  </section>

  <section class="spine">
    <p class="spine-text">Lanterns Along the Harbor Road<span class="spine-author">&nbsp;&nbsp;Dale Purvin</span></p>
  </section>

  <section class="front-cover">
    <div class="front-scene" role="img" aria-label="Erupting volcano with glowing lava under a stormy magenta sky with lightning, a rocky slope and a stone path in the foreground"></div>
    <h1 class="front-title">
      <span class="front-title__line front-title__line--first">Lanterns Along</span>
      <span class="front-title__line front-title__line--second">The Harbor Road</span>
    </h1>
    <p class="front-subtitle">
      <span class="front-subtitle__line">Quiet Lessons from an Orchard</span>
      <span class="front-subtitle__line">Keeper and Her Curious</span>
      <span class="front-subtitle__line front-subtitle__line--last">Village Neighbors</span>
    </p>
    <p class="front-author">Dale Purvin</p>
  </section>

</div>
</body>
</html>
```